Powerpoint for Talveo

Check out the attached sample powerpoint, we would like our powerpoint to look similar to this. in the slides where you see monitor, we would like to put pics of different industries in each monitor. like images of hotels, hospitals, large business with multiple locations, small business, retail)

The Powerpoint will contain the below slides

About US
Our Guarantee – 100% satisfaction and 30% cost savings
Products & Services ( Hosted PBX phone system, SIP Trunking, Network security solutions, commercial grade band width and firewalls, IT Network design services)
Features ( One slide for this we will enter the content)
Industries ( Small business, hospitality, hospitals, Banks for secure voice, Large business with multiple locations, Retail)
Hosted PBX
Why Talveo
Channel partners
Our customers
Contact us
Updates

Target Market(s)

Small business, hospitality, hospitals, Banks for secure voice, Large business with multiple locations, Retail, law firms, insurance companies

Industry/Entity Type

Security

Requirements
Must have
• Please look at the attached powerpoint for color, style, font details

```html
<!DOCTYPE html>
<html lang="en">
<head>
<meta charset="utf-8">
<title>Talveo – Presentation Template</title>
<link href="https://fonts.googleapis.com/css2?family=Carlito:wght@400;700&display=swap" rel="stylesheet">
<style>
  :root{
    --canvas:#ffffff;
    --ink:#231f20;
    --dark:#231f20;
    --grey:#bcbdc0;
    --blue:#00aeef;
    --green:#8dc63f;
    --pink:#ec008c;
    --orange:#f7941d;
    --yellow:#fff200;
    --row-tint:#e3eed6;
    --row-light:#f1f6ea;
    --shadow:0 2px 5px rgba(0,0,0,.35);
  }
  *{box-sizing:border-box;margin:0;padding:0}
  html,body{width:1200px;height:690px;overflow:hidden;background:var(--canvas)}
  body{position:relative;font-family:"Carlito","Calibri",sans-serif;color:var(--ink)}
  .slide{position:absolute;background:#fff;box-shadow:var(--shadow);overflow:hidden}
  .slide--title{left:16px;top:58px;width:376px;height:281px}
  .slide--text{left:405px;top:58px;width:377px;height:282px}
  .slide--graphic{left:798px;top:58px;width:382px;height:288px}
  .slide--table{left:16px;top:353px;width:377px;height:285px}
  .slide--closing{left:405px;top:355px;width:379px;height:285px}

  .band-dark{position:absolute;left:0;right:0;background:var(--dark)}
  .band-grey{position:absolute;left:0;right:0;bottom:0;background:var(--grey)}
  .title-box{position:absolute;left:0;background:var(--blue);color:#fff;display:flex;align-items:center;padding-left:8px}
  .subtitle{position:absolute;left:8px;font-size:11px;color:var(--ink)}

  .brand{position:absolute;display:flex;align-items:center;gap:3px;font-weight:700;color:var(--dark)}
  .brand__mark{background:var(--pink)}

  .bubble-art{position:absolute;border-radius:6px;
    background:radial-gradient(circle at 30% 40%,rgba(141,198,63,.55),transparent 45%),
               radial-gradient(circle at 70% 30%,rgba(236,0,140,.5),transparent 45%),
               radial-gradient(circle at 55% 75%,rgba(255,242,0,.45),transparent 45%),
               radial-gradient(circle at 85% 70%,rgba(0,174,239,.45),transparent 40%),
               radial-gradient(circle at 15% 80%,rgba(247,148,29,.45),transparent 40%)}
  .corner-art{position:absolute;border-radius:4px;
    background:linear-gradient(135deg,rgba(247,148,29,.55),rgba(141,198,63,.5) 40%,rgba(255,242,0,.55) 65%,rgba(236,0,140,.5))}

  .slide-header{position:absolute;left:0;top:0;right:0;height:53px;background:var(--dark);color:#fff;font-size:16px;display:flex;align-items:center;padding-left:14px}
  .slide-footer{position:absolute;left:0;right:0;bottom:0;height:11px;background:var(--blue);color:#fff;font-size:5px;display:flex;align-items:center;justify-content:space-between;padding:0 10px 0 10px}
  .slide-footer span:nth-child(2){position:absolute;left:50%;transform:translateX(-50%)}

  .bullets{position:absolute;list-style:none;font-size:10.5px;line-height:1.25}
  .bullets li{position:relative;padding-left:14px;margin-bottom:5px}
  .bullets li::before{content:"•";position:absolute;left:0;color:var(--green)}
  .bullets li.sub{padding-left:30px;font-size:9.5px}
  .bullets li.sub::before{content:"–";left:17px}

  .section-title{position:absolute;left:0;right:0;text-align:center;color:var(--green);font-size:10.5px}

  .data-table{position:absolute;left:53px;top:136px;border-collapse:collapse;font-size:8.5px}
  .data-table th{background:var(--green);color:#fff;font-weight:700;height:15px;padding:0 4px;border-right:1px solid #fff}
  .data-table td{height:15px;text-align:center;width:54px;border-right:1px solid #fff;border-top:1px solid #fff}
  .data-table tr:nth-child(odd) td{background:var(--row-tint)}
  .data-table tr:nth-child(even) td{background:var(--row-light)}

  .contacts{position:absolute;left:8px;bottom:20px;width:280px;font-size:6px;line-height:1.35;color:#fff}
  .contacts b{color:var(--ink)}
</style>
</head>
<body>

<section class="slide slide--title">
  <div class="brand" style="right:8px;top:22px;font-size:15px"><span class="brand__mark" style="width:8px;height:8px"></span>Talveo</div>
  <div class="band-dark" style="top:60px;height:172px"></div>
  <div class="bubble-art" role="img" aria-label="Cluster of colourful speech bubbles" style="left:212px;top:66px;width:162px;height:152px"></div>
  <div class="title-box" style="top:132px;width:192px;height:43px;font-size:16px">Presentation Title</div>
  <div class="band-grey" style="height:49px"></div>
  <p class="subtitle" style="top:245px">Presentation Subtitle</p>
</section>

<section class="slide slide--text">
  <header class="slide-header">Text Slide</header>
  <ul class="bullets" style="left:14px;top:62px;right:10px">
    <li>Lorem ipsum dolor sit amet, consectetur adipiscing elit.</li>
    <li>Cras vitae tincidunt felis.</li>
    <li>Vestibulum eget risus nec justo consequat tincidunt eget non tellus.</li>
    <li class="sub">Donec in orci eu turpis condimentum ultricies.</li>
    <li>Sed placerat aliquam tortor ac ultricies.</li>
    <li class="sub">Morbi ultrices sem at libero imperdiet facilisis. Aliquam sagittis magna nec venenatis tristique.</li>
    <li class="sub">Sed non sem elit.</li>
    <li>Suspendisse in congue ante, ac cursus enim. Fusce viverra quam turpis, convallis congue urna commodo eu.</li>
  </ul>
  <div class="corner-art" role="img" aria-label="Small speech bubble accents" style="left:4px;top:232px;width:34px;height:32px"></div>
  <div class="brand" style="right:10px;bottom:16px;font-size:8px"><span class="brand__mark" style="width:5px;height:5px"></span>Talveo</div>
  <footer class="slide-footer"><span>16-11-2013</span><span>Confidential</span><span>2</span></footer>
</section>

<section class="slide slide--graphic">
  <header class="slide-header">Graphic Slide</header>
  <h2 class="section-title" style="top:63px;font-weight:400">Graphic Title</h2>
  <ul class="bullets" style="left:14px;top:81px;right:30px">
    <li>Lorem ipsum dolor sit amet, consectetur adipiscing elit. Cras vitae tincidunt felis.</li>
  </ul>
  <svg style="position:absolute;left:0;top:0" width="382" height="288" viewBox="0 0 382 288" font-family="Carlito, sans-serif" font-size="7" fill="#231f20" text-anchor="middle">
    <line x1="70" y1="242" x2="320" y2="242" stroke="#bcbdc0" stroke-width="0.8"/>
    <g>
      <rect x="79" y="138" width="13" height="104" fill="var(--blue)"/><text x="85.5" y="134">4,3</text>
      <rect x="93" y="184" width="13" height="58" fill="var(--green)"/><text x="99.5" y="180">2,4</text>
      <rect x="107" y="194" width="13" height="48" fill="var(--pink)"/><text x="113.5" y="190">2</text>
      <text x="99.5" y="256" font-size="8">2010</text>
    </g>
    <g>
      <rect x="140" y="182" width="13" height="60" fill="var(--blue)"/><text x="146.5" y="178">2,5</text>
      <rect x="154" y="136" width="13" height="106" fill="var(--green)"/><text x="160.5" y="132">4,4</text>
      <rect x="168" y="194" width="13" height="48" fill="var(--pink)"/><text x="174.5" y="190">2</text>
      <text x="160.5" y="256" font-size="8">2011</text>
    </g>
    <g>
      <rect x="201" y="157" width="13" height="85" fill="var(--blue)"/><text x="207.5" y="153">3,5</text>
      <rect x="215" y="198" width="13" height="44" fill="var(--green)"/><text x="221.5" y="194">1,8</text>
      <rect x="229" y="169" width="13" height="73" fill="var(--pink)"/><text x="235.5" y="165">3</text>
      <text x="221.5" y="256" font-size="8">2012</text>
    </g>
    <g>
      <rect x="262" y="133" width="13" height="109" fill="var(--blue)"/><text x="268.5" y="129">4,5</text>
      <rect x="276" y="174" width="13" height="68" fill="var(--green)"/><text x="282.5" y="170">2,8</text>
      <rect x="290" y="121" width="13" height="121" fill="var(--pink)"/><text x="296.5" y="117">5</text>
      <text x="282.5" y="256" font-size="8">2013</text>
    </g>
  </svg>
  <div class="corner-art" role="img" aria-label="Small speech bubble accents" style="left:4px;top:234px;width:38px;height:34px"></div>
  <div class="brand" style="right:10px;bottom:20px;font-size:8px"><span class="brand__mark" style="width:5px;height:5px"></span>Talveo</div>
  <footer class="slide-footer"><span>16-11-2013</span><span>Confidential</span><span>3</span></footer>
</section>

<section class="slide slide--table">
  <header class="slide-header">Table slide</header>
  <h2 class="section-title" style="top:64px;font-weight:400">Table Title</h2>
  <ul class="bullets" style="left:14px;top:82px;right:30px">
    <li>Lorem ipsum dolor sit amet, consectetur adipiscing elit. Cras vitae tincidunt felis.</li>
  </ul>
  <table class="data-table">
    <thead><tr><th>Category A</th><th>Category B</th><th>Category C</th><th>Category D</th><th>Category E</th></tr></thead>
    <tbody>
      <tr><td>555.999</td><td>333.444</td><td>777.333</td><td>444.555</td><td>111.222</td></tr>
      <tr><td>111.222</td><td>111.222</td><td>333.444</td><td>555.999</td><td>777.333</td></tr>
      <tr><td>333.444</td><td>555.999</td><td>111.222</td><td>777.333</td><td>555.999</td></tr>
      <tr><td>111.222</td><td>777.333</td><td>555.666</td><td>111.222</td><td>333.444</td></tr>
    </tbody>
  </table>
  <div class="corner-art" role="img" aria-label="Small speech bubble accents" style="left:3px;top:234px;width:38px;height:32px"></div>
  <div class="brand" style="right:10px;bottom:18px;font-size:8px"><span class="brand__mark" style="width:5px;height:5px"></span>Talveo</div>
  <footer class="slide-footer"><span>16-11-2013</span><span>Confidential</span><span>4</span></footer>
</section>

<section class="slide slide--closing">
  <div class="brand" style="right:8px;top:24px;font-size:15px"><span class="brand__mark" style="width:8px;height:8px"></span>Talveo</div>
  <div class="band-dark" style="top:60px;height:173px"></div>
  <div class="bubble-art" role="img" aria-label="Cluster of colourful speech bubbles" style="left:214px;top:70px;width:162px;height:148px"></div>
  <div class="title-box" style="top:133px;width:195px;height:43px;font-size:14px">THANK YOU FOR YOUR TIME</div>
  <div class="band-grey" style="height:52px"></div>
  <p class="contacts"><b>Contacts:</b> Integer bibendum lacinia vulputate. Proin sit amet tellus sit amet lacus feugiat volutpat nec et nisi. Vestibulum dapibus mi ante, ut interdum nisi sodales sit amet.</p>
</section>

</body>
</html>
```